I want a business letter head designed, one that I can have printed but also one that I can use as an insert for proforma documentation that is printed in house.

Business name : RJ Penfold & Associates
Address: PO Box 738
Tewantin Qld 4587

Type of business: Accounting practice- accounting, taxation, audit, self managed superannuation,

Colour scheme: black and blue - previously designed a business card; however the blue that is one the cards is very washed out and I am not particularly happy with it.

Industry/Entity Type

Business

```html
<!DOCTYPE html>
<html lang="en">
<head>
<meta charset="utf-8">
<title>RJ Penfold &amp; Associates — Letterhead</title>
<link rel="stylesheet" href="https://fonts.googleapis.com/css2?family=Arimo&display=swap">
<style>
  :root {
    --backdrop: #0aa6e8;
    --paper: #ffffff;
    --ink-black: #050505;
    --brand-blue: #0797f5;
    --watermark-blue: #bfe3fb;
    --text-white: #ffffff;
  }
  html, body {
    margin: 0;
    width: 1200px;
    height: 1013px;
    overflow: hidden;
    background: var(--backdrop);
  }
  .letterhead {
    position: absolute;
    left: 266px;
    top: 26px;
    width: 668px;
    height: 960px;
    display: block;
  }
  .paper { fill: var(--paper); }
  .header-band { fill: var(--ink-black); }
  .footer-band { fill: var(--brand-blue); }
  .brand-square { fill: var(--brand-blue); }
  .footer-square { fill: var(--text-white); }
  .business-name,
  .contact-line,
  .services-line,
  .footer-name,
  .watermark-name {
    font-family: "Arimo", Arial, sans-serif;
    font-weight: 400;
  }
  .business-name { font-size: 10px; fill: var(--text-white); }
  .contact-line { font-size: 5.6px; fill: var(--text-white); }
  .services-line { font-size: 6.6px; fill: var(--text-white); }
  .footer-name { font-size: 6.6px; fill: var(--text-white); }
  .watermark-name { font-size: 25px; fill: var(--watermark-blue); }
</style>
</head>
<body>
<svg class="letterhead" viewBox="0 0 431 619" preserveAspectRatio="none" role="img" aria-label="RJ Penfold &amp; Associates letterhead">
  <rect class="paper" x="0" y="0" width="431" height="619"/>
  <polygon class="header-band" points="0,0 431,0 431,4 0,117"/>
  <polygon class="footer-band" points="0,616 431,500 431,619 0,619"/>

  <text class="watermark-name" x="222" y="306" text-anchor="middle">RJ Penfold &amp; Associates</text>

  <rect class="brand-square" x="36" y="14" width="34" height="34"/>
  <text class="business-name" x="80" y="35">RJ Penfold &amp; Associates</text>
  <text class="contact-line" x="36" y="59">PO Box 738 Tewantin Qld 4587</text>
  <text class="contact-line" x="36" y="72">email: office@rjpenfoldassociates.com.au</text>

  <rect class="footer-square" x="404" y="574" width="14" height="14"/>
  <text class="footer-name" x="398" y="584" text-anchor="end">RJ Penfold &amp; Associates</text>
  <text class="services-line" x="105" y="611">Accounting  . Taxation  . Audit  . Self Managed  . Superannuation</text>
</svg>
</body>
</html>
```